Double-sided half page marketing handout for professional association conference

We need a collatoral piece that will go into conference attendees' registration packets. Handout will be double-sided, half-letter-sized page. Working print area is 8.1" by 5.3" for each side. Can be laid out either vertically or horizontally.

One side of the piece will be focused on my firm's contact information and broad scope of services:

Contact Information:
Halvick Partners LLC
Local Government Consultants
555-314-0297
www.halvickpartners.example
info@halvickpartners.example

Services:
Bond Rating Assessments
Economic Development Consulting
Executive Dashboards
Public Policy Analysis
Governance Training & Support
Strategic Planning & Performance Management

The other side of the piece will focus on the Bond Rating Assessments (see http://www.halvickpartners.example/Pages/Bond-Rating-Assessments.aspx and attachments for more detail). This side should contain the text:

"Considering issuing debt? Bond ratings make a difference. Did you know that on an average $20 million GO debt issuance a one rating-level difference can easily equate to over $350,000 in interest cost-savings under normal market conditions?

The ratings agencies use a combined quantitative and qualitative approach to arrive at your bond rating. Our Bond Ratings Assessment shows you precisely what the agencies are looking at, provides advice as to how to frame the conversation during ratings calls, and identifies both strategic opportunities to provide upgrade pressure and specific threats that may lead to a downgrade. Call or email us to find out more or to get an example assessment."

Go to www.halvickpartners.example and see attached files for logo and a recent winning ArtBazaarly 1/4 page advertisement for style guidance.

Target Market(s)

Highly-educated, conservative local government executives.

Industry/Entity Type

Marketing

Font styles to use
Sans Serif

Colors
3277b5
85acd3
ffffff

Requirements
Must have
• Our logo, our contact information, basic information stated in Project Description. Feel free to modify language to make more clear or understandable.
Nice to have
• We rather not just a text piece - bringing in some graphical elements would be very nice.

```html
<!DOCTYPE html>
<html lang="en">
<head>
<meta charset="utf-8">
<title>Halvick Partners LLC – Bond Rating Assessments</title>
<link rel="stylesheet" href="https://fonts.googleapis.com/css2?family=Arimo:wght@400&family=Roboto+Condensed:wght@400;700&display=swap">
<style>
  :root {
    --frame-blue: #1010e8;
    --panel-blue: #3385ef;
    --accent-blue: #3a86ee;
    --ink: #111111;
    --paper: #ffffff;
  }
  html, body {
    margin: 0;
    padding: 0;
    width: 1200px;
    height: 840px;
    overflow: hidden;
    background: var(--paper);
  }
  .handout {
    position: relative;
    width: 1200px;
    height: 840px;
    font-family: "Arimo", Arial, sans-serif;
  }
  .panel-shape {
    position: absolute;
    inset: 0;
  }
  .contact-side {
    position: absolute;
    left: 7px;
    top: 72px;
    width: 574px;
    text-align: center;
    color: var(--paper);
  }
  .contact-side h2 {
    margin: 0 0 2px;
    font-weight: 400;
    font-size: 31px;
    line-height: 36px;
  }
  .contact-side p {
    margin: 0;
    font-size: 22px;
    line-height: 29.6px;
  }
  .contact-side .services-title { margin-top: 26px; }
  .brand {
    position: absolute;
    left: 108px;
    top: 560px;
    width: 371px;
    height: 200px;
    display: flex;
    align-items: center;
    justify-content: center;
    gap: 12px;
    font-family: "Arimo", Arial, sans-serif;
    font-size: 30px;
    color: var(--ink);
  }
  .brand-mark {
    width: 22px;
    height: 22px;
    background: var(--ink);
  }
  .headline-box {
    position: absolute;
    left: 625px;
    top: 10px;
    width: 565px;
    height: 138px;
    box-sizing: border-box;
    border: 9px solid var(--frame-blue);
    background: var(--panel-blue);
    color: var(--paper);
    font-family: "Roboto Condensed", "Arial Narrow", sans-serif;
    font-size: 35px;
    line-height: 44px;
    text-align: center;
    display: flex;
    align-items: center;
    justify-content: center;
    margin: 0;
    font-weight: 400;
  }
  .body-copy {
    position: absolute;
    left: 635px;
    top: 177px;
    width: 560px;
    margin: 0;
    font-size: 21.5px;
    line-height: 29.8px;
    color: var(--ink);
    white-space: nowrap;
  }
  .divider {
    position: absolute;
    left: 640px;
    top: 580px;
    width: 533px;
    height: 6px;
    background: var(--accent-blue);
  }
  .cta-box {
    position: absolute;
    left: 623px;
    top: 657px;
    width: 567px;
    height: 181px;
    box-sizing: border-box;
    border: 8px solid var(--accent-blue);
    background: var(--paper);
    color: var(--accent-blue);
    font-family: "Roboto Condensed", "Arial Narrow", sans-serif;
    font-weight: 700;
    font-size: 37px;
    line-height: 44.5px;
    text-align: center;
    display: flex;
    align-items: center;
    justify-content: center;
    margin: 0;
    letter-spacing: -0.5px;
  }
</style>
</head>
<body>
<main class="handout">
  <svg class="panel-shape" width="1200" height="840" viewBox="0 0 1200 840" aria-hidden="true">
    <path d="M7,42 H581 V604 H479 V560 H108 V604 H7 Z" fill="var(--panel-blue)" stroke="var(--frame-blue)" stroke-width="7"/>
    <path d="M7,691 H108 V760 H479 V691 H581 V810 H7 Z" fill="var(--panel-blue)" stroke="var(--frame-blue)" stroke-width="7"/>
  </svg>

  <section class="contact-side">
    <h2>Contact Information:</h2>
    <p>Halvick Partners LLC</p>
    <p>Local Government Consultants</p>
    <p>555-314-0297</p>
    <p>www.halvickpartners.example</p>
    <p>info@halvickpartners.example</p>
    <h2 class="services-title">Services:</h2>
    <p>Bond Rating Assessments</p>
    <p>Economic Development Consulting</p>
    <p>Executive Dashboards</p>
    <p>Public Policy Analysis</p>
    <p>Governance Training &amp; Support</p>
    <p>Strategic Planning &amp; Performance Management</p>
  </section>

  <div class="brand"><span class="brand-mark"></span>Halvick Partners LLC</div>

  <h1 class="headline-box">Considering issuing debt?<br>Bond ratings make a difference.</h1>

  <p class="body-copy">Did you know that on an average $20 million GO<br>debt issuance a one rating-level difference can<br>easily equate to over $350,000 in interest<br>cost-savings under normal market conditions?<br>The ratings agencies use a combined quantitative<br>and qualitative approach to arrive at your bond<br>rating.Our Bond Ratings Assessment shows you<br>precisely what the agencies are looking at,<br>provides advice as to how to frame the<br>conversation during ratings calls,and identifies<br>both strategic opportunities to provide upgrade<br>pressure and specific threats that may lead to<br>a downgrade.</p>

  <div class="divider"></div>

  <p class="cta-box">Call or email us<br>to find out more or to get an<br>example assessment.</p>
</main>
</body>
</html>
```